Brightpath Wellness Referral Program

We have recently started a referral program for our clinics and we need a postcard that we can hand our to clients to let them know about the new program.
We are looking for a 4x6" card design that highlights our incentive referral program while visually either showing some of the services we offer, or, conveying a message of health, community, family, etc.
The details of our referral program can be found at:
https://brightpathwellness.ca/about/refer-a-friend.html
We would also like to see somewhere on the card, 2 lines for:
1) Your name: ( new clients name)
2) Referred by: __________
The card can be single or double sided, whatever looks best for design purposes.
Target Market(s)
Ages 20-50, equal men and women
Look and feel
Each slider illustrates characteristics of the customer's brand and the style your logo design should communicate.

```html
<!DOCTYPE html>
<html lang="en">
<head>
<meta charset="utf-8">
<title>Brightpath Wellness Referral Program Postcard</title>
<link rel="stylesheet" href="https://fonts.googleapis.com/css2?family=Montserrat:wght@800;900&family=Roboto:ital,wght@0,400;0,700;1,400;1,700&display=swap">
<style>
  :root {
    --brand-blue: #0a6ab0;
    --brand-blue-deep: #0c4f8c;
    --headline-ghost: #3a8bcb;
    --ink: #2b2b2b;
    --ink-soft: #444;
    --paper: #ffffff;
    --backdrop: #eceae6;
  }
  * { box-sizing: border-box; margin: 0; padding: 0; }
  html, body { width: 1200px; height: 923px; overflow: hidden; }
  body {
    background: var(--backdrop);
    position: relative;
    font-family: "Roboto", Arial, sans-serif;
    color: var(--ink);
  }
  .card {
    position: absolute;
    width: 600px;
    height: 400px;
    background: var(--paper);
    overflow: hidden;
    box-shadow: 0 6px 18px rgba(0,0,0,.18);
  }
  .card--front { left: 70px; top: 40px; }
  .card--back { left: 530px; top: 478px; }
  .layer { position: absolute; inset: 0; }

  /* shared */
  .brand-name {
    position: absolute;
    font-family: "Roboto", Arial, sans-serif;
    font-weight: 400;
    display: flex; align-items: center; gap: 8px;
    white-space: nowrap;
  }
  .brand-name__dot { width: 14px; height: 14px; border-radius: 50%; }
  .earn-badge { position: absolute; }
  .earn-badge text { font-family: "Montserrat", Arial, sans-serif; font-weight: 900; }

  /* front */
  .card--front .brand-name { left: 30px; top: 40px; font-size: 22px; color: var(--paper); }
  .card--front .brand-name__dot { background: var(--paper); width: 12px; height: 12px; }
  .massage-photo {
    position: absolute; left: 0; top: 95px; width: 250px; height: 170px;
    background: radial-gradient(ellipse at 45% 50%, rgba(12,79,140,.55), rgba(10,106,176,0) 70%);
  }
  .referral-form { position: absolute; left: 48px; top: 262px; width: 240px; }
  .form-field { margin-bottom: 18px; }
  .form-field__label { font-weight: 700; font-size: 13px; color: var(--ink); }
  .form-field__line { margin-top: 16px; border-bottom: 1.5px dotted var(--ink-soft); }
  .form-field__hint { font-style: italic; font-size: 7px; text-align: center; margin-top: 4px; color: var(--ink-soft); }
  .card--front .earn-badge { left: 290px; top: 315px; }

  /* back */
  .ghost-headline {
    position: absolute; left: 24px; top: 2px;
    font-family: "Montserrat", Arial, sans-serif; font-weight: 900;
    font-size: 37px; line-height: 27px; color: var(--headline-ghost);
    opacity: .75; letter-spacing: 1px;
  }
  .announce-pill {
    position: absolute; left: -20px; top: 141px; width: 255px; height: 38px;
    border: 1.5px solid var(--paper); border-radius: 0 20px 20px 0;
    padding: 4px 0 0 42px;
    font-family: "Montserrat", Arial, sans-serif; font-weight: 900;
    font-size: 14px; line-height: 14px; color: var(--paper);
  }
  .program-title {
    position: absolute; left: 20px; top: 186px;
    font-family: "Montserrat", Arial, sans-serif; font-weight: 900;
    font-size: 35px; line-height: 32px; color: var(--paper);
  }
  .intro {
    position: absolute; left: 260px; top: 22px; width: 312px;
    color: var(--paper); font-size: 12px; line-height: 15px;
  }
  .intro p + p { margin-top: 7px; }
  .card--back .earn-badge--south { left: 252px; top: 120px; }
  .card--back .earn-badge--north { left: 402px; top: 120px; }
  .reward-note {
    position: absolute; top: 208px; width: 128px;
    font-style: italic; font-weight: 700; font-size: 8px; line-height: 10px; color: var(--paper);
  }
  .reward-note--south { left: 260px; }
  .reward-note--north { left: 410px; }
  .credits-copy {
    position: absolute; left: 20px; top: 292px; width: 565px;
    font-size: 11.6px; line-height: 15.5px; color: var(--ink);
  }
  .fine-print {
    position: absolute; left: 20px; top: 345px; width: 392px;
    font-style: italic; font-size: 5.6px; line-height: 8.3px; color: var(--ink-soft);
    text-align: justify;
  }
  .card--back .brand-name { left: 430px; top: 355px; font-size: 15px; color: var(--brand-blue); }
  .card--back .brand-name__dot { background: var(--brand-blue); width: 10px; height: 10px; }
</style>
</head>
<body>

<!-- Front of card -->
<section class="card card--front" aria-label="Postcard front">
  <svg class="layer" viewBox="0 0 600 400" aria-hidden="true">
    <defs>
      <linearGradient id="front-fade" x1="0" y1="0" x2="0" y2="1">
        <stop offset="0" stop-color="#0a6ab0"/>
        <stop offset=".55" stop-color="#1f74b6"/>
        <stop offset=".78" stop-color="#b9d3e9"/>
        <stop offset="1" stop-color="#ffffff"/>
      </linearGradient>
    </defs>
    <rect width="600" height="400" fill="url(#front-fade)"/>
    <path d="M400 0 C300 40 235 130 232 220 C230 300 300 370 400 400 L600 400 L600 0 Z" fill="#ffffff"/>
    <path d="M418 0 C320 44 255 132 252 220 C250 298 315 366 412 400 L418 400 C330 366 272 298 272 220 C275 135 340 50 440 0 Z" fill="#d5d7da"/>
  </svg>
  <div class="massage-photo" role="img" aria-label="Photo of a client relaxing face-down during a massage, tinted blue"></div>
  <svg class="layer" viewBox="0 0 600 400" role="img" aria-label="Photo of a surprised young woman holding a fan of cash and pointing at it">
    <defs>
      <linearGradient id="photo-tone" x1="0" y1="0" x2="1" y2="1">
        <stop offset="0" stop-color="#e9edf1"/>
        <stop offset=".6" stop-color="#dfe6ee"/>
        <stop offset="1" stop-color="#b9cfe6"/>
      </linearGradient>
    </defs>
    <path d="M445 8 C345 50 282 135 280 220 C278 296 335 362 425 400 L600 400 L600 0 L470 0 Z" fill="url(#photo-tone)"/>
  </svg>
  <div class="brand-name"><span class="brand-name__dot"></span>Brightpath Wellness</div>
  <div class="referral-form">
    <div class="form-field">
      <div class="form-field__label">Name:</div>
      <div class="form-field__line"></div>
      <div class="form-field__hint">(new clients name)</div>
    </div>
    <div class="form-field">
      <div class="form-field__label">Referred by:</div>
      <div class="form-field__line"></div>
    </div>
  </div>
  <svg class="earn-badge" width="118" height="76" viewBox="0 0 118 76" aria-label="Earn $25">
    <ellipse cx="59" cy="38" rx="56" ry="35" fill="#ffffff" stroke="#0a6ab0" stroke-width="3"/>
    <text x="86" y="25" text-anchor="middle" font-size="13" fill="#0a6ab0">Earn</text>
    <text x="58" y="62" text-anchor="middle" font-size="40" fill="#0a6ab0">$25</text>
  </svg>
</section>

<!-- Back of card -->
<section class="card card--back" aria-label="Postcard back">
  <svg class="layer" viewBox="0 0 600 400" aria-hidden="true">
    <defs>
      <linearGradient id="back-blue" x1="0" y1="0" x2="0" y2="1">
        <stop offset="0" stop-color="#0a6ab0"/>
        <stop offset="1" stop-color="#0c4f8c"/>
      </linearGradient>
    </defs>
    <path d="M0 0 H600 V186 C520 258 380 284 240 282 C130 280 45 262 0 240 Z" fill="#a9abae"/>
    <path d="M0 0 H600 V180 C520 248 380 274 240 272 C120 270 40 250 0 222 Z" fill="url(#back-blue)"/>
  </svg>
  <div class="ghost-headline" aria-hidden="true">GOOD<br>PEOPLE<br>KNOW<br>GOOD<br>PEOPLE</div>
  <div class="announce-pill">ANNOUNCING OUR<br>NEWLY REDESIGNED</div>
  <h1 class="program-title">REFERRAL<br>PROGRAM</h1>
  <div class="intro">
    <p>Referrals are the <b>lifeblood</b> of our small business.</p>
    <p>We are <b>incredibly grateful</b> for your trust and recommendations over the years, and we want to show our gratitude. That's why we are introducing an exciting new way to earn more free treatment. Now you can:</p>
  </div>
  <svg class="earn-badge earn-badge--south" width="118" height="78" viewBox="0 0 118 78" aria-label="Earn $25">
    <ellipse cx="59" cy="39" rx="55" ry="35" fill="#ffffff" stroke="#9fb3c8" stroke-width="3"/>
    <text x="84" y="22" text-anchor="middle" font-size="12" fill="#0a6ab0">Earn</text>
    <text x="58" y="60" text-anchor="middle" font-size="38" fill="#0a6ab0">$25</text>
  </svg>
  <svg class="earn-badge earn-badge--north" width="118" height="78" viewBox="0 0 118 78" aria-label="Earn $10">
    <ellipse cx="59" cy="39" rx="55" ry="35" fill="#ffffff" stroke="#9fb3c8" stroke-width="3"/>
    <text x="84" y="22" text-anchor="middle" font-size="12" fill="#0a6ab0">Earn</text>
    <text x="58" y="60" text-anchor="middle" font-size="38" fill="#0a6ab0">$10</text>
  </svg>
  <p class="reward-note reward-note--south">for every referral you make to our south Maplecrest location (Harbourview Drive), and;</p>
  <p class="reward-note reward-note--north">for every referral you make to our north Maplecrest location (Northgate).</p>
  <p class="credits-copy">Credits can be <b>used for any service at either our north or south location</b> and, in the spirit of community, <b>credits are transferable</b>. Refer 4 people to the south and you could gift someone a $100 gift card! Or, enjoy a well deserved, free treatment yourself.</p>
  <p class="fine-print">*Referral(s) must be brand new client(s) to the Brightpath Wellness Inc. practice, having never booked or attended an appointment at any Brightpath Wellness location. Referral must attend their appointment for you to be eligible for a referral credit. Referral credit value is dependent upon which Brightpath Wellness location your referral attends: you are eligible for a $10 credit for a referral to our north location (#410 - 1520 Cedar Ridge Road NW); you are eligible for a $25 credit for a referral to our south location (#120 - 3300 Willow Bend Drive SE). We are really good at asking but please remind your referral to tell us it is YOU who we have to thank! Credit(s) may be redeemed as payment or partial payment for any service at any Brightpath Wellness location. Credits have no cash value and no expiry.</p>
  <div class="brand-name"><span class="brand-name__dot"></span>Brightpath Wellness</div>
</section>

</body>
</html>
```